Business Card Design Project

I need a business card design for our new logo, please check the logo at the following link:
https://www.filecrate.net/s/q7rtx2pw9kd41m/FernLoop.png
The address on the business card:
Av. Gervásio Tavares 418 sala 207
Barra da Tijuca, Rio de Janeiro, RJ
CEP: 22714-380
Brasil
Phone: +55 21 86347215
e-mail: osvaldo@fernloop.com.br
Updates
Thank you all for sending your designs, we will not provide feedback because there are too many designs, on December 3 we will pick the best design according to our point of view. Please keep posting.
Osvaldo
Industry/Entity Type
Business
Look and feel
Each slider illustrates characteristics of the customer's brand and the style your logo design should communicate.

```html
<!DOCTYPE html>
<html lang="pt-BR">
<head>
<meta charset="utf-8">
<title>FernLoop – Cartão de Visita</title>
<link href="https://fonts.googleapis.com/css2?family=Share+Tech+Mono&family=Pinyon+Script&display=swap" rel="stylesheet">
<style>
  :root {
    --purple: #932b8e;
    --purple-deep: #7e2376;
    --purple-strip: #7b2574;
    --band: #0e1212;
    --ink: #1b1b1b;
    --mascot-light: #4a2a48;
    --mascot-dark: #2c1f2c;
    --accent: #f6c400;
  }
  * { margin: 0; padding: 0; box-sizing: border-box; }
  html, body { width: 1200px; height: 673px; overflow: hidden; background: #ffffff; }
  .card {
    position: relative;
    width: 1200px;
    height: 673px;
    background: var(--purple);
    overflow: hidden;
    font-family: "Share Tech Mono", monospace;
    color: var(--ink);
  }
  .card__backdrop { position: absolute; inset: 0; }
  .mascot {
    position: absolute;
    left: 78px; top: 20px;
    width: 388px; height: 300px;
    border-radius: 28px;
    background: linear-gradient(160deg, var(--mascot-light) 0%, var(--mascot-dark) 100%);
  }
  .brand-name {
    position: absolute;
    left: 50px; top: 370px;
    display: flex;
    align-items: center;
    gap: 18px;
  }
  .brand-name__dot {
    width: 40px; height: 40px;
    background: var(--accent);
  }
  .brand-name__text {
    font-size: 80px;
    line-height: 1;
    letter-spacing: 2px;
    color: var(--ink);
  }
  .brand-script {
    position: absolute;
    left: 500px; top: 62px;
    font-family: "Pinyon Script", cursive;
    font-size: 118px;
    line-height: 1;
    color: var(--ink);
    white-space: nowrap;
  }
  .address {
    position: absolute;
    left: 536px; top: 206px;
    font-style: normal;
  }
  .address__street {
    display: block;
    font-size: 24px;
    letter-spacing: 7.2px;
    transform: scaleX(0.86);
    transform-origin: left;
    white-space: nowrap;
  }
  .address__line {
    display: block;
    margin-left: 45px;
    font-size: 24px;
    letter-spacing: 1.5px;
    line-height: 36px;
    white-space: nowrap;
  }
  .address__street + .address__line { margin-top: 8px; }
  .contact {
    position: absolute;
    top: 587px; left: 0;
    width: 100%; height: 62px;
  }
  .contact__item { display: flex; align-items: center; position: absolute; top: 0; height: 62px; }
  .contact__item--email { left: 70px; }
  .contact__item--phone { left: 566px; }
  .contact__text { font-size: 22px; letter-spacing: 4px; color: var(--ink); white-space: nowrap; }
  .contact__item--email .contact__text { margin-left: 14px; }
  .contact__item--phone .contact__text { margin-left: 22px; font-size: 26px; letter-spacing: 6px; }
</style>
</head>
<body>
<div class="card">
  <svg class="card__backdrop" width="1200" height="673" viewBox="0 0 1200 673" aria-hidden="true">
    <path d="M0 387 Q250 460 527 451 Q950 437 1200 179 L1200 511 L0 511 Z" fill="var(--purple-deep)"/>
    <rect x="0" y="511" width="1200" height="67" fill="var(--band)"/>
    <rect x="0" y="578" width="1200" height="95" fill="var(--purple-strip)"/>
  </svg>

  <div class="mascot" role="img" aria-label="Illustration of the brand mascot running with a briefcase"></div>
  <div class="brand-name">
    <span class="brand-name__dot" aria-hidden="true"></span>
    <span class="brand-name__text">FernLoop</span>
  </div>

  <div class="brand-script">FernLoop</div>
  <address class="address">
    <span class="address__street">Av. Gervásio Tavares 418 sala 207</span>
    <span class="address__line">Barra da Tijuca, Rio de Janeiro, RJ</span>
    <span class="address__line">CEP: 22714-380</span>
    <span class="address__line">Brasil</span>
  </address>

  <div class="contact">
    <div class="contact__item contact__item--email">
      <svg width="52" height="31" viewBox="0 0 52 31" aria-hidden="true">
        <rect x="1.5" y="1.5" width="49" height="28" fill="none" stroke="var(--ink)" stroke-width="2.5"/>
        <path d="M1.5 1.5 L26 18 L50.5 1.5 M1.5 29.5 L20 14 M50.5 29.5 L32 14" fill="none" stroke="var(--ink)" stroke-width="2.5"/>
      </svg>
      <span class="contact__text">osvaldo@fernloop.com.br</span>
    </div>
    <div class="contact__item contact__item--phone">
      <svg width="32" height="62" viewBox="0 0 32 62" aria-hidden="true">
        <rect x="4" y="1" width="3" height="12" fill="var(--ink)"/>
        <rect x="2" y="12" width="28" height="48" rx="5" fill="none" stroke="var(--ink)" stroke-width="2.5"/>
        <rect x="7" y="17" width="18" height="14" fill="none" stroke="var(--ink)" stroke-width="2"/>
        <g fill="var(--ink)">
          <rect x="7" y="35" width="4" height="4"/><rect x="14" y="35" width="4" height="4"/><rect x="21" y="35" width="4" height="4"/>
          <rect x="7" y="42" width="4" height="4"/><rect x="14" y="42" width="4" height="4"/><rect x="21" y="42" width="4" height="4"/>
          <rect x="7" y="49" width="4" height="4"/><rect x="14" y="49" width="4" height="4"/><rect x="21" y="49" width="4" height="4"/>
        </g>
      </svg>
      <span class="contact__text">+55 21 86347215</span>
    </div>
  </div>
</div>
</body>
</html>
```